"Use it or Lose it" and "Brush on Over"

We are a dental office looking to connect with our patients through direct mail advertising. With the last 3 months of the year coming we would like to send out Post Cards to our patients letting them know they have 3 months left to "USE IT OR LOSE IT" when it comes to their dental insurance benefits.
So we are looking for a post card that has the "Use It or Lost it" theme along with our dental office logo, telephone number and address.

We are also looking for a post card that says "Brush On Over" to remind our patients that they are due for a dental cleaning and we would like for them to come over to our dental office for a well needed cleaning :).

```html
<!DOCTYPE html>
<html lang="en">
<head>
<meta charset="utf-8">
<title>Linwood Dental – Use It or Lose It Postcard</title>
<link rel="stylesheet" href="https://fonts.googleapis.com/css2?family=Montserrat:wght@400;700;800&family=Lato:wght@400&display=swap">
<style>
  :root {
    --page-bg: #d1d2d4;
    --card-bg: #ffffff;
    --ink: #000000;
    --brand-blue: #1a5fa8;
    --brand-blue-light: #3d8fd4;
    --brand-blue-dark: #0f4f8f;
    --stamp-grey: #c6c5c7;
    --rule-grey: #8a8a8a;
    --text-grey: #3a3a3a;
  }
  * { margin: 0; padding: 0; box-sizing: border-box; }
  html, body { width: 1200px; height: 1200px; overflow: hidden; }
  body { background: var(--page-bg); position: relative; font-family: "Lato", sans-serif; }

  .postcard { position: absolute; left: 172px; width: 856px; background: var(--card-bg); overflow: hidden; }
  .postcard--front { top: 45px; height: 549px; }
  .postcard--back { top: 632px; height: 544px; }

  .brand-name {
    position: absolute; left: 22px; top: 26px;
    display: flex; align-items: center; gap: 10px;
    font-family: "Montserrat", sans-serif; font-weight: 700;
    font-size: 26px; letter-spacing: 1px; color: var(--brand-blue);
  }
  .brand-name__dot { width: 30px; height: 30px; border-radius: 50%; background: var(--brand-blue); }

  .headline {
    position: absolute; left: 40px; font-family: "Montserrat", sans-serif;
    font-weight: 800; font-size: 88px; line-height: 1; color: var(--ink); letter-spacing: -1px;
  }
  .headline--first { top: 176px; }
  .headline--second { top: 290px; }

  .illustration {
    position: absolute; left: 316px; top: 26px; width: 512px; height: 374px;
    background: radial-gradient(ellipse at 60% 25%, var(--brand-blue-light) 0%, var(--brand-blue) 45%, rgba(26,95,168,0.08) 80%, rgba(255,255,255,0) 100%);
    border-radius: 50% 50% 12px 12px / 60% 60% 12px 12px;
  }

  .offer-band {
    position: absolute; left: 0; top: 433px; width: 100%; height: 116px;
    background: var(--ink); color: #fff; display: flex; align-items: center; justify-content: center;
    text-align: center; font-family: "Montserrat", sans-serif; font-weight: 400;
    font-size: 21px; line-height: 26px; letter-spacing: 0.3px;
  }

  .brand-feature {
    position: absolute; left: 40px; top: 30px; width: 352px; height: 320px;
    display: flex; flex-direction: column; align-items: center; justify-content: center; gap: 22px;
    font-family: "Montserrat", sans-serif; font-weight: 700; font-size: 40px; line-height: 1.1;
    color: var(--brand-blue); text-align: center; letter-spacing: 1px;
  }
  .brand-feature__dot { width: 120px; height: 120px; border-radius: 50%; background: var(--brand-blue); }

  .divider { position: absolute; left: 431px; top: 8px; width: 2px; height: 352px; background: #444; border-radius: 1px; }
  .stamp-box { position: absolute; left: 692px; top: 16px; width: 104px; height: 118px; background: var(--stamp-grey); }
  .address-label { position: absolute; left: 494px; top: 156px; font-size: 15px; color: var(--text-grey); }
  .address-line { position: absolute; left: 503px; width: 293px; height: 1px; background: var(--rule-grey); }
  .address-line--1 { top: 223px; } .address-line--2 { top: 266px; } .address-line--3 { top: 307px; }

  .contact-item { position: absolute; display: flex; align-items: center; gap: 20px; font-size: 20px; color: var(--text-grey); }
  .contact-item--web { left: 23px; top: 378px; }
  .contact-item--fax { left: 327px; top: 378px; gap: 22px; }
  .contact-item--phone { left: 581px; top: 381px; gap: 22px; }
  .contact-icon { width: 35px; height: 35px; border-radius: 50%; background: var(--brand-blue-dark); display: flex; align-items: center; justify-content: center; flex-shrink: 0; }
  .contact-icon svg { width: 17px; height: 17px; }

  .location-band { position: absolute; left: 0; top: 427px; width: 100%; height: 117px; background: var(--ink); }
  .location-item { position: absolute; left: 20px; display: flex; align-items: center; gap: 25px; font-size: 20px; color: #fff; letter-spacing: 0.3px; }
  .location-item--address { top: 16px; }
  .location-item--email { top: 67px; }
  .location-icon { width: 36px; height: 36px; border-radius: 50%; background: #fff; display: flex; align-items: center; justify-content: center; }
  .location-icon svg { width: 18px; height: 18px; }
</style>
</head>
<body>

<section class="postcard postcard--front">
  <div class="brand-name"><span class="brand-name__dot"></span>LINWOOD DENTAL</div>
  <div class="illustration" role="img" aria-label="Illustration of a smiling cartoon tooth holding a large blue umbrella"></div>
  <h1 class="headline headline--first">USE IT</h1>
  <h1 class="headline headline--second">OR LOSE IT</h1>
  <div class="offer-band"><p>USE YOUR DENTAL INSURANCE BENEFIT BEFORE<br>31ST DECEMBER OR YOU LOSE THEM</p></div>
</section>

<section class="postcard postcard--back">
  <div class="brand-feature"><span class="brand-feature__dot"></span>LINWOOD<br>DENTAL</div>
  <div class="divider"></div>
  <div class="stamp-box"></div>
  <p class="address-label">To</p>
  <div class="address-line address-line--1"></div>
  <div class="address-line address-line--2"></div>
  <div class="address-line address-line--3"></div>

  <div class="contact-item contact-item--web">
    <span class="contact-icon"><svg viewBox="0 0 20 20" fill="none" stroke="#fff" stroke-width="1.8"><circle cx="10" cy="10" r="8"/><path d="M2 10h16M10 2c3 3 3 13 0 16M10 2c-3 3-3 13 0 16"/></svg></span>
    <span>linwooddental.com</span>
  </div>
  <div class="contact-item contact-item--fax">
    <span class="contact-icon"><svg viewBox="0 0 20 20" fill="#fff"><rect x="5" y="2" width="10" height="6"/><rect x="2" y="8" width="16" height="8" rx="1"/><rect x="5" y="12" width="10" height="6" fill="#0f4f8f" stroke="#fff" stroke-width="1.5"/></svg></span>
    <span>201 - 555 - 0148</span>
  </div>
  <div class="contact-item contact-item--phone">
    <span class="contact-icon"><svg viewBox="0 0 20 20" fill="#fff"><path d="M5 2l3 4-2 2c1 2.5 3.5 5 6 6l2-2 4 3-2 3C9 18 2 11 2 4z"/></svg></span>
    <span>201 - 555 - 0172</span>
  </div>

  <div class="location-band">
    <div class="location-item location-item--address">
      <span class="location-icon"><svg viewBox="0 0 20 20" fill="#000"><path d="M10 1a6 6 0 0 0-6 6c0 5 6 12 6 12s6-7 6-12a6 6 0 0 0-6-6zm0 8.5a2.5 2.5 0 1 1 0-5 2.5 2.5 0 0 1 0 5z"/></svg></span>
      <span>58 Maple Court Linwood, NJ 07000</span>
    </div>
    <div class="location-item location-item--email">
      <span class="location-icon"><svg viewBox="0 0 20 20"><rect x="2" y="4" width="16" height="12" rx="1.5" fill="#000"/><path d="M3 5.5l7 5.5 7-5.5" fill="none" stroke="#fff" stroke-width="1.6"/></svg></span>
      <span>linwooddental@mail.com</span>
    </div>
  </div>
</section>

</body>
</html>
```